This will be the mural for Sydney's Premier new Fitness Facility

After a printed sticker (wall decal) to cover 2.5m x 3m.
Basically we want lots of descriptive words in different fonts running in several lines. see attached pic of something similar. However in that long list of words we want 4 words to be in orange, those words all start with the letter D. examples of that would be dedication, discipline, drive, dream etc, (all very motivating sporting words) The other words in white or silver, all about sport, motivating, rehabilitation or health.
Somehow we would like the 7K logo involved, either at the top, or behind or behind on an angle or something so you can tell you are at 7K.

7K is a health and performance clinic that deal with injuries and sporting performance. www.7kvw.example

Target Market(s)

athletes, general fitness, injury patients

Industry/Entity Type

Fitness

Colors
f37122
ffffff

Requirements
Must have
• 7K logo involved somehow so everyone can see it,
• 4 words starting with letter D in orange
Nice to have
• we can change the words after rits designed, but basically words like rehabilitation, performance, health, speed, strength, motivation etc

```html
<!DOCTYPE html>
<html lang="en">
<head>
<meta charset="utf-8">
<title>7K Motivation Wall Mural</title>
<link rel="stylesheet" href="https://fonts.googleapis.com/css2?family=Bebas+Neue&display=swap">
<style>
  :root {
    --wall: #ececec;
    --decal: #ffffff;
    --silver: #a9a9a9;
    --orange: #d24c06;
  }
  html, body {
    margin: 0;
    padding: 0;
    width: 1157px;
    height: 1200px;
    overflow: hidden;
    background: var(--wall);
  }
  .mural {
    position: absolute;
    left: 0;
    top: 119px;
    width: 1157px;
    height: 962px;
    display: block;
  }
  .mural__panel { fill: var(--decal); }
  .word {
    font-family: "Bebas Neue", "Oswald", sans-serif;
    fill: var(--silver);
  }
  .word--d { fill: var(--orange); }
  .brand-mark {
    font-family: "Bebas Neue", "Oswald", sans-serif;
    fill: var(--orange);
  }
</style>
</head>
<body>
<svg class="mural" viewBox="0 0 1230 1023" xmlns="http://www.w3.org/2000/svg" role="img" aria-label="7K motivation word wall">
  <rect class="mural__panel" x="0" y="0" width="1230" height="1023"/>

  <g class="words words--horizontal">
    <text class="word word--d" x="12" y="66" font-size="57" textLength="108" lengthAdjust="spacingAndGlyphs">DRIVE</text>
    <text class="word" x="142" y="66" font-size="54" textLength="208" lengthAdjust="spacingAndGlyphs">CHALLENGE</text>
    <text class="word" x="15" y="168" font-size="121" textLength="338" lengthAdjust="spacingAndGlyphs">VITAMIN</text>
    <text class="word" x="448" y="100" font-size="117" textLength="270" lengthAdjust="spacingAndGlyphs">FOCUS</text>
    <text class="word" x="448" y="165" font-size="74" textLength="275" lengthAdjust="spacingAndGlyphs">CHALLENGE</text>
    <text class="word" x="450" y="308" font-size="186" textLength="205" lengthAdjust="spacingAndGlyphs">EAT</text>
    <text class="word" x="450" y="358" font-size="60" textLength="207" lengthAdjust="spacingAndGlyphs">CHALLENGE</text>
    <text class="word word--d" x="835" y="85" font-size="96" textLength="378" lengthAdjust="spacingAndGlyphs">DISCIPLINE</text>
    <text class="word" x="833" y="143" font-size="71" textLength="382" lengthAdjust="spacingAndGlyphs">TRANSFORMATION</text>
    <text class="word" x="835" y="256" font-size="140" textLength="385" lengthAdjust="spacingAndGlyphs">HEALTHY</text>
    <text class="word" x="835" y="313" font-size="67" textLength="165" lengthAdjust="spacingAndGlyphs">POWER</text>
    <text class="word" x="1005" y="383" font-size="164" textLength="208" lengthAdjust="spacingAndGlyphs">RUN</text>
    <text class="word" x="80" y="228" font-size="71" textLength="163" lengthAdjust="spacingAndGlyphs">DREAM</text>
    <text class="word" x="245" y="226" font-size="57" textLength="115" lengthAdjust="spacingAndGlyphs">GOALS</text>
    <text class="word" x="80" y="296" font-size="76" textLength="273" lengthAdjust="spacingAndGlyphs">CHALLENGE</text>
    <text class="word" x="338" y="420" font-size="67" textLength="139" lengthAdjust="spacingAndGlyphs">GOALS</text>
    <text class="word" x="487" y="418" font-size="64" textLength="220" lengthAdjust="spacingAndGlyphs">HARDWORK</text>
    <text class="word word--d" x="335" y="573" font-size="200" textLength="458" lengthAdjust="spacingAndGlyphs">DREAM</text>
    <text class="word word--d" x="998" y="456" font-size="61" textLength="215" lengthAdjust="spacingAndGlyphs">DISCIPLINE</text>
    <text class="word" x="890" y="588" font-size="157" textLength="333" lengthAdjust="spacingAndGlyphs">FOCUS</text>
    <text class="word" x="890" y="653" font-size="81" textLength="110" lengthAdjust="spacingAndGlyphs">RUN</text>
    <text class="word" x="890" y="738" font-size="100" textLength="205" lengthAdjust="spacingAndGlyphs">DRIVE</text>
    <text class="word" x="13" y="516" font-size="83" textLength="100" lengthAdjust="spacingAndGlyphs">EAT</text>
    <text class="word" x="13" y="608" font-size="107" textLength="220" lengthAdjust="spacingAndGlyphs">FOCUS</text>
    <text class="word" x="13" y="670" font-size="71" textLength="402" lengthAdjust="spacingAndGlyphs">TRANSFORMATION</text>
    <text class="word" x="423" y="670" font-size="71" textLength="230" lengthAdjust="spacingAndGlyphs">DISCIPLINE</text>
    <text class="word" x="13" y="718" font-size="46" textLength="132" lengthAdjust="spacingAndGlyphs">SUCCESS</text>
    <text class="word" x="270" y="750" font-size="100" textLength="380" lengthAdjust="spacingAndGlyphs">CHALLENGE</text>
    <text class="word" x="15" y="803" font-size="100" textLength="135" lengthAdjust="spacingAndGlyphs">RUN</text>
    <text class="word" x="275" y="801" font-size="50" textLength="272" lengthAdjust="spacingAndGlyphs">TRANSFORMATION</text>
    <text class="word" x="17" y="900" font-size="114" textLength="140" lengthAdjust="spacingAndGlyphs">EAT</text>
    <text class="word" x="273" y="896" font-size="119" textLength="284" lengthAdjust="spacingAndGlyphs">DREAM</text>
    <text class="word" x="735" y="846" font-size="137" textLength="372" lengthAdjust="spacingAndGlyphs">VITAMIN</text>
    <text class="word" x="653" y="928" font-size="86" textLength="340" lengthAdjust="spacingAndGlyphs">CHALLENGE</text>
    <text class="word" x="658" y="1008" font-size="93" textLength="212" lengthAdjust="spacingAndGlyphs">DREAM</text>
    <text class="word" x="880" y="1006" font-size="90" textLength="120" lengthAdjust="spacingAndGlyphs">RUN</text>
    <text class="word word--d" x="13" y="1000" font-size="110" textLength="402" lengthAdjust="spacingAndGlyphs">DEDICATION</text>
    <text class="word" x="428" y="950" font-size="49" textLength="129" lengthAdjust="spacingAndGlyphs">VITAMIN</text>
    <text class="word" x="428" y="1000" font-size="63" textLength="129" lengthAdjust="spacingAndGlyphs">GOALS</text>
  </g>

  <g class="words words--vertical">
    <text class="word" transform="translate(365 18) rotate(90)" font-size="107" textLength="335" lengthAdjust="spacingAndGlyphs">NUTRITION</text>
    <text class="word" transform="translate(725 18) rotate(90)" font-size="150" textLength="280" lengthAdjust="spacingAndGlyphs">GOALS</text>
    <text class="word" transform="translate(670 170) rotate(90)" font-size="71" textLength="183" lengthAdjust="spacingAndGlyphs">HEALTHY</text>
    <text class="word" transform="translate(13 183) rotate(90)" font-size="81" textLength="255" lengthAdjust="spacingAndGlyphs">EXERCISE</text>
    <text class="word" transform="translate(115 313) rotate(90)" font-size="164" textLength="200" lengthAdjust="spacingAndGlyphs">RUN</text>
    <text class="word" transform="translate(253 316) rotate(90)" font-size="89" textLength="292" lengthAdjust="spacingAndGlyphs">NUTRITION</text>
    <text class="word" transform="translate(953 323) rotate(90)" font-size="50" textLength="135" lengthAdjust="spacingAndGlyphs">EXERCISE</text>
    <text class="word" transform="translate(800 463) rotate(90)" font-size="114" textLength="275" lengthAdjust="spacingAndGlyphs">ENERGY</text>
    <text class="word" transform="translate(657 586) rotate(90)" font-size="90" textLength="257" lengthAdjust="spacingAndGlyphs">EXERCISE</text>
    <text class="word" transform="translate(743 586) rotate(90)" font-size="49" textLength="152" lengthAdjust="spacingAndGlyphs">HARDWORK</text>
    <text class="word" transform="translate(160 678) rotate(90)" font-size="133" textLength="235" lengthAdjust="spacingAndGlyphs">MOVE</text>
    <text class="word" transform="translate(570 768) rotate(90)" font-size="107" textLength="235" lengthAdjust="spacingAndGlyphs">POWER</text>
    <text class="word" transform="translate(1117 608) rotate(90)" font-size="143" textLength="395" lengthAdjust="spacingAndGlyphs">SUCCESS</text>
    <text class="word" transform="translate(1005 856) rotate(90)" font-size="50" textLength="154" lengthAdjust="spacingAndGlyphs">HARDWORK</text>
    <text class="word" transform="translate(1055 856) rotate(90)" font-size="50" textLength="152" lengthAdjust="spacingAndGlyphs">NUTRITION</text>
  </g>

  <g class="brand">
    <text class="brand-mark brand-mark--large" x="715" y="456" font-size="200" textLength="225" lengthAdjust="spacingAndGlyphs">7K</text>
    <text class="brand-mark brand-mark--small" x="1015" y="648" font-size="69" textLength="82" lengthAdjust="spacingAndGlyphs">7K</text>
  </g>
</svg>
</body>
</html>
```